Business Card Design Project

1. Show the company logo.
2. Only company email ID and website address to be shown (office@zolotoyveter.fm , www.zolotoyveter.fm).
3. Logo to be provided by us, 2 designs just in case. The logo is made with ' Zolotoy Veter' text, need to be edited so that it shows 'Tikhaya Gavan' instead .
4. Single sided business card, portrait or landscape is not a problem; back side to be filled with colors or a design that matches the logo the best.
5. Logo is to be embossed.
6. We're looking at an English and Russian version.
7. any other better idea is always welcomed.

```html
<!DOCTYPE html>
<html lang="en">
<head>
<meta charset="utf-8">
<title>Zolotoy Veter — Business Card</title>
<link rel="stylesheet" href="https://fonts.googleapis.com/css2?family=Nunito:wght@400;700;800&display=swap">
<style>
  :root {
    --page: #ffffff;
    --card-blue: #0b5fa5;
    --band-light: #4a8fc7;
    --ring-mid: #0a5a9c;
    --logo-navy: #0c3674;
    --text-white: #ffffff;
    --text-pale: #a9cdec;
    --text-faint: #2f74b5;
  }
  * { margin: 0; padding: 0; box-sizing: border-box; }
  html, body {
    width: 1052px;
    height: 1200px;
    overflow: hidden;
    background: var(--page);
    font-family: "Nunito", sans-serif;
  }
  .sheet { position: relative; width: 1052px; height: 1200px; }
  .card {
    position: absolute;
    left: 176px;
    width: 700px;
    height: 400px;
    overflow: hidden;
    background: var(--card-blue);
    box-shadow: 0 4px 14px rgba(0, 0, 0, 0.12);
  }
  .card--front { top: 150px; }
  .card--back { top: 660px; }
  .card__art { position: absolute; inset: 0; width: 100%; height: 100%; }

  .logo-name {
    position: absolute;
    color: var(--text-pale);
    font-weight: 700;
    line-height: 1.1;
    text-align: center;
    text-transform: uppercase;
  }
  .card--front .logo-name {
    left: 60px;
    top: 150px;
    width: 220px;
    font-size: 28px;
  }
  .card--back .logo-name {
    left: 60px;
    top: 158px;
    width: 280px;
    font-size: 40px;
  }

  .contact {
    position: absolute;
    color: var(--text-white);
    font-weight: 800;
    font-size: 24px;
    white-space: nowrap;
  }
  .contact--web { top: 50px; left: 372px; }
  .contact--mail { top: 262px; left: 350px; }

  .company {
    position: absolute;
    left: 372px;
    top: 118px;
    color: var(--text-pale);
    line-height: 1.05;
  }
  .company__first {
    display: block;
    font-weight: 800;
    font-size: 30px;
    text-transform: uppercase;
  }
  .company__second {
    display: block;
    font-weight: 400;
    font-size: 34px;
  }

  .faint-name {
    position: absolute;
    left: 470px;
    top: 150px;
    color: var(--text-faint);
    line-height: 1.05;
  }
  .faint-name .company__first { font-size: 32px; }
  .faint-name .company__second { font-size: 36px; }
</style>
</head>
<body>
<main class="sheet">

  <section class="card card--front" aria-label="Card front">
    <svg class="card__art" viewBox="0 0 700 400" aria-hidden="true">
      <rect width="700" height="400" fill="var(--card-blue)"/>
      <path d="M360 0 H700 V45 H520 Q430 30 360 0 Z" fill="var(--band-light)"/>
      <path d="M0 0 H120 Q40 140 20 400 H0 Z" fill="var(--band-light)"/>
      <path d="M520 400 Q620 330 700 340 V400 Z" fill="var(--band-light)"/>
      <path d="M170 400 L200 300 L250 300 L280 400 Z" fill="var(--band-light)"/>
      <circle cx="170" cy="175" r="172" fill="var(--band-light)"/>
      <circle cx="170" cy="175" r="148" fill="var(--ring-mid)"/>
      <circle cx="170" cy="175" r="136" fill="var(--logo-navy)"/>
    </svg>
    <p class="logo-name">Zolotoy<br>Veter</p>
    <p class="contact contact--web">www.zolotoyveter.fm</p>
    <p class="company">
      <span class="company__first">Tikhaya</span>
      <span class="company__second">Gavan</span>
    </p>
    <p class="contact contact--mail">office@zolotoyveter.fm</p>
  </section>

  <section class="card card--back" aria-label="Card back">
    <svg class="card__art" viewBox="0 0 700 400" aria-hidden="true">
      <rect width="700" height="400" fill="var(--band-light)"/>
      <path d="M400 0 H700 V400 H440 Q540 200 400 0 Z" fill="var(--card-blue)"/>
      <path d="M320 400 L350 330 L400 340 L390 400 Z" fill="var(--card-blue)"/>
      <circle cx="170" cy="200" r="262" fill="var(--band-light)"/>
      <circle cx="170" cy="200" r="240" fill="var(--ring-mid)"/>
      <circle cx="170" cy="200" r="226" fill="var(--logo-navy)"/>
    </svg>
    <p class="logo-name">Tikhaya<br>Gavan</p>
    <p class="faint-name">
      <span class="company__first">Tikhaya</span>
      <span class="company__second">Gavan</span>
    </p>
  </section>

</main>
</body>
</html>
```